Graphics for Vorlani telehealth weight loss plans

Vorlani focuses on delivering medical weight-loss using prescription medicine and telehealth consults. Vorlani needs graphics for its ecommerce site for three weight loss plans. The plans are posted here with current graphics and descriptions of what is included with each plan. Please do not feel constrained by current graphics or styling.

- https://shop.vorlanicare.com/products/steady-horizon-plan
- https://shop.vorlanicare.com/products/amber-ridge-plan
- https://shop.vorlanicare.com/products/calm-harbor-plan

The graphics need to look good on mobile and desktop browsers.

```html
<!DOCTYPE html>
<html lang="en">
<head>
<meta charset="utf-8">
<title>Vorlani – Calm Harbor Plan</title>
<link rel="stylesheet" href="https://fonts.googleapis.com/css2?family=Quicksand:wght@500&family=Fira+Sans+Condensed:wght@500;600&display=swap">
<style>
  :root {
    --purple-light: #8a63c6;
    --purple-mid: #6e4bb0;
    --purple-deep: #4f3390;
    --orange: #f47a10;
    --orange-soft: #e58a3a;
    --white: #ffffff;
    --shadow: rgba(20, 8, 40, 0.55);
    --photo-skin: #e7c3ae;
    --photo-hair: #c9a074;
  }
  * { margin: 0; padding: 0; box-sizing: border-box; }
  html, body { width: 1200px; height: 1200px; overflow: hidden; }
  body { font-family: "Fira Sans Condensed", sans-serif; color: var(--white); }

  .plan-card {
    position: relative;
    width: 1200px;
    height: 1200px;
    overflow: hidden;
    background: radial-gradient(ellipse at 30% 30%, var(--purple-light) 0%, var(--purple-mid) 45%, var(--purple-deep) 100%);
  }
  .backdrop-photo {
    position: absolute; inset: 0;
    background: radial-gradient(ellipse 300px 520px at 700px 760px, rgba(60, 35, 110, 0.45), transparent 70%),
                radial-gradient(ellipse 260px 380px at 300px 260px, rgba(200, 180, 235, 0.35), transparent 70%);
  }
  .model-photo {
    position: absolute;
    left: 0; top: 312px;
    width: 440px; height: 774px;
    background: linear-gradient(180deg, var(--photo-hair) 0%, var(--photo-skin) 35%, #f2ede9 62%, var(--photo-skin) 80%, #2a2230 100%);
    border-radius: 0 180px 0 0;
    opacity: 0.9;
  }

  .brand-mark {
    position: absolute;
    left: 46px; top: 48px;
    width: 192px; height: 162px;
    border: 3px solid var(--white);
    display: flex; align-items: center; justify-content: center;
    font-weight: 600;
    font-size: 48px;
    letter-spacing: 1px;
    color: var(--white);
  }

  .plan-title {
    position: absolute;
    left: 286px; top: 24px;
    font-family: "Quicksand", sans-serif;
    font-weight: 500;
    font-size: 136px;
    line-height: 122px;
    letter-spacing: -4px;
    white-space: nowrap;
    text-shadow: 4px 4px 5px var(--shadow);
  }
  .plan-title .accent { color: var(--orange); margin-right: 36px; }

  .title-rule {
    position: absolute;
    left: 296px; top: 302px;
    width: 848px; height: 5px;
    background: linear-gradient(90deg, var(--orange) 0%, var(--orange-soft) 50%, rgba(229, 138, 58, 0) 100%);
  }

  .plan-intro {
    position: absolute;
    left: 464px; top: 336px;
    width: 720px;
    font-weight: 600;
    font-size: 52px;
    line-height: 55px;
    white-space: nowrap;
  }
  .plan-intro .highlight { color: var(--orange); }

  .plan-features {
    position: absolute;
    left: 462px; top: 652px;
    width: 730px;
    list-style: none;
    font-weight: 500;
    font-size: 51px;
    line-height: 54px;
  }
  .plan-features li {
    position: relative;
    padding-left: 60px;
  }
  .plan-features li::before {
    content: "";
    position: absolute;
    left: 0; top: 16px;
    width: 27px; height: 27px;
    background: var(--orange);
  }

  .shop-band {
    position: absolute;
    left: 0; top: 1086px;
    width: 1200px; height: 114px;
    background: linear-gradient(90deg, var(--orange) 0%, #c8723f 45%, var(--purple-mid) 100%);
  }
  .shop-link {
    position: absolute;
    left: 176px; top: 1100px;
    font-weight: 600;
    font-size: 64px;
    line-height: 80px;
    color: var(--white);
    text-decoration: none;
  }
</style>
</head>
<body>
  <main class="plan-card">
    <div class="backdrop-photo" role="img" aria-label="Tinted photo of a fit woman's figure in leggings, faded into the purple background"></div>
    <div class="model-photo" role="img" aria-label="Photo of a slim young woman with blonde hair in a white sports bra"></div>

    <div class="brand-mark">Vorlani</div>

    <h1 class="plan-title">Calm<br><span class="accent">Harbor</span>Plan</h1>
    <div class="title-rule"></div>

    <p class="plan-intro">This plan is designed for<br>people who need to <span class="highlight">“lose a<br>few pounds”</span>, and who want<br>expert consultation for overall<br>health, and vitality</p>

    <ul class="plan-features">
      <li>Expert nutrition consult</li>
      <li>Custom crafted diet plan to<br>achieve your goals</li>
      <li>Nutrition coaching to improve<br>your health and vitality</li>
      <li>100% online</li>
      <li>Month-to-month pay as you go</li>
    </ul>

    <div class="shop-band"></div>
    <a class="shop-link" href="https://shop.vorlanicare.com">https://shop.vorlanicare.com</a>
  </main>
</body>
</html>
```